Carver Lindqvist Group Business Cards

We have a new logo, and want to design new business cards with it. We are 21 years in business, and want a fresh but professional look, so not a lot of extra stuff on the card. We are a recruiting and staffing firm focused on placing accounting and finance professionals in the Dallas TX area. I've attached our new logo that should be displayed on the cards. Here is what I think we want on the cards:
Ray Pemberly, CPA
Partner and Managing Director
8282 Orchard Vale Rd.
Suite 610
Dallas, TX 75391
O 214-555-0184
M 214-555-0237
ray@carverlindqvist.example
www.carverlindqvist.example

```html
<!DOCTYPE html>
<html lang="en">
<head>
<meta charset="utf-8">
<title>Carver Lindqvist Group – Business Cards</title>
<link href="https://fonts.googleapis.com/css2?family=Roboto:wght@300;400;500;700&display=swap" rel="stylesheet">
<style>
  :root {
    --brand-blue: #2543a6;
    --brand-blue-light: #5b7fcf;
    --paper: #ffffff;
    --stage: #e9ebef;
    --ink-light: #ffffff;
  }
  * { box-sizing: border-box; margin: 0; padding: 0; }
  html, body {
    width: 1200px; height: 900px; overflow: hidden;
    background: var(--stage);
    font-family: "Roboto", Arial, sans-serif;
  }
  .sheet {
    width: 1200px; height: 900px;
    display: flex; flex-direction: column;
    align-items: center; justify-content: center; gap: 60px;
  }
  .card {
    position: relative;
    width: 600px; height: 343px;
    overflow: hidden;
    box-shadow: 0 6px 18px rgba(20, 30, 60, 0.18);
  }
  .card-back { background: var(--brand-blue); }
  .card-front { background: var(--paper); }

  .bands { position: absolute; inset: 0; }

  .wordmark {
    display: flex; align-items: center; gap: 12px;
    font-weight: 700; letter-spacing: 0.5px; line-height: 1.05;
    text-transform: uppercase;
  }
  .wordmark-square { width: 18px; height: 18px; flex: none; }
  .card-back .wordmark {
    position: absolute; left: 50%; top: 50%;
    transform: translate(-50%, -50%);
    color: var(--ink-light); font-size: 34px; white-space: nowrap;
  }
  .card-back .wordmark-square { background: var(--ink-light); }

  .identity {
    position: absolute; left: 34px; top: 14px; color: var(--ink-light);
  }
  .identity-name { font-size: 19px; font-weight: 700; }
  .identity-title { font-size: 14px; font-weight: 300; margin-top: 3px; }

  .contact-list {
    position: absolute; left: 30px; top: 104px;
    list-style: none; display: flex; flex-direction: column; gap: 12px;
    color: var(--brand-blue); font-size: 15px;
  }
  .contact-item { display: flex; align-items: center; gap: 10px; }
  .contact-icon {
    width: 26px; height: 26px; border-radius: 50%;
    background: var(--brand-blue); flex: none;
    display: flex; align-items: center; justify-content: center;
  }
  .contact-icon svg { width: 14px; height: 14px; }

  .card-front .wordmark {
    position: absolute; left: 318px; top: 140px;
    color: var(--brand-blue); font-size: 25px; width: 250px;
  }
  .card-front .wordmark-square { background: var(--brand-blue); }

  .address {
    position: absolute; right: 28px; bottom: 14px;
    text-align: right; color: var(--ink-light);
    font-size: 16px; line-height: 1.3; font-style: normal;
  }
</style>
</head>
<body>
<main class="sheet">

  <section class="card card-back" aria-label="Card back">
    <div class="wordmark">
      <span class="wordmark-square"></span>
      <span>Carver Lindqvist Group</span>
    </div>
  </section>

  <section class="card card-front" aria-label="Card front">
    <svg class="bands" viewBox="0 0 600 343" preserveAspectRatio="none" aria-hidden="true">
      <polygon points="0,0 600,0 600,26 360,26 330,70 0,70" fill="var(--brand-blue-light)"/>
      <polygon points="0,0 600,0 600,14 348,14 318,70 0,70" fill="var(--brand-blue)"/>
      <polygon points="0,317 240,317 270,265 600,265 600,343 0,343" fill="var(--brand-blue-light)"/>
      <polygon points="0,329 252,329 282,265 600,265 600,343 0,343" fill="var(--brand-blue)"/>
    </svg>

    <div class="identity">
      <p class="identity-name">Ray Pemberly, CPA</p>
      <p class="identity-title">Partner and Managing Director</p>
    </div>

    <ul class="contact-list">
      <li class="contact-item">
        <span class="contact-icon"><svg viewBox="0 0 24 24"><path fill="#fff" d="M6.6 10.8a15.1 15.1 0 0 0 6.6 6.6l2.2-2.2c.3-.3.7-.4 1-.2 1.1.4 2.3.6 3.6.6.6 0 1 .4 1 1V20c0 .6-.4 1-1 1A17 17 0 0 1 3 4c0-.6.4-1 1-1h3.5c.6 0 1 .4 1 1 0 1.3.2 2.5.6 3.6.1.3 0 .7-.2 1z"/></svg></span>
        <span>Office: 214-555-0184</span>
      </li>
      <li class="contact-item">
        <span class="contact-icon"><svg viewBox="0 0 24 24"><rect x="6" y="2" width="12" height="20" rx="2" fill="none" stroke="#fff" stroke-width="2"/><circle cx="12" cy="18" r="1.3" fill="#fff"/></svg></span>
        <span>Mobile: 214-555-0237</span>
      </li>
      <li class="contact-item">
        <span class="contact-icon"><svg viewBox="0 0 24 24"><rect x="2" y="5" width="20" height="14" rx="1" fill="#fff"/><path d="M2 6l10 7 10-7" fill="none" stroke="var(--brand-blue)" stroke-width="1.8"/></svg></span>
        <span>ray@carverlindqvist.example</span>
      </li>
      <li class="contact-item">
        <span class="contact-icon"><svg viewBox="0 0 24 24" fill="none" stroke="#fff" stroke-width="1.8"><circle cx="12" cy="12" r="9"/><ellipse cx="12" cy="12" rx="4" ry="9"/><path d="M3 12h18M5 7h14M5 17h14"/></svg></span>
        <span>www.carverlindqvist.example</span>
      </li>
    </ul>

    <div class="wordmark">
      <span class="wordmark-square"></span>
      <span>Carver Lindqvist Group</span>
    </div>

    <address class="address">
      8282 Orchard Vale Rd.<br>
      Suite 610, Dallas, TX 75391
    </address>
  </section>

</main>
</body>
</html>
```